Redesign website for small print company

Vindabrot is a small printing company in Iceland mainly servicing Students, schools, etc. We are also doing all kind of other jobs, like business cards, book printing, brochure printing etc. We are also selling books online.
Our website is: www.vindabrot.is
What we are looking for is:
- Web Design (Uncoded - PSD layout only)
- Mobile friendly design, using our current color scheme: Red, green, yellow and light gray.
- Clean simple design
- Simple, light and easy to use.
- More menu Items/drop down
Industry/Entity Type
Digital Printing
Number of Pages Required
5+ page
Requirements
Must have
- Easy navigation
- Designed for mobile
- Current color scheme (see logo)
Nice to have
- Icon based products

```html
<!DOCTYPE html>
<html lang="en">
<head>
<meta charset="utf-8">
<title>Vindabrot – Printing Services</title>
<link href="https://fonts.googleapis.com/css2?family=Raleway:wght@400;500;600;700&family=Open+Sans:wght@400;600&display=swap" rel="stylesheet">
<style>
:root{
  --red:#c93a2b;
  --ink:#1d1d1d;
  --text:#333;
  --muted:#555;
  --line:#d8d8d8;
  --black:#0e0e0e;
  --white:#fff;
}
*{margin:0;padding:0;box-sizing:border-box}
html,body{width:1200px;height:3279px;overflow:hidden}
body{position:relative;background:var(--white);font-family:"Open Sans",Arial,sans-serif;color:var(--text)}
.abs{position:absolute}
.title{font-family:"Raleway",Arial,sans-serif;color:var(--red);font-weight:500;font-size:25px;text-align:center;left:0;width:1200px}
.title::after{content:"";display:block;width:46px;height:2px;background:var(--red);margin:12px auto 0}
.btn{background:var(--red);color:var(--white);font-family:"Raleway",Arial,sans-serif;font-weight:600;font-size:14px;display:flex;align-items:center;justify-content:center}

/* header */
.header{top:0;left:0;width:1200px;height:100px;background:var(--white);box-shadow:0 2px 6px rgba(0,0,0,.08);z-index:2}
.brand{left:130px;top:14px;display:flex;flex-direction:column;align-items:center;gap:6px}
.brand-mark{width:40px;height:40px;background:var(--red)}
.brand-name{font-family:"Raleway",Arial,sans-serif;font-weight:700;font-size:12px;color:var(--ink);letter-spacing:.5px}
.topline{top:8px;left:830px;font-size:12px;display:flex;gap:10px;align-items:center}
.topline .call{color:var(--red)}
.nav{top:40px;left:284px;font-family:"Raleway",Arial,sans-serif;font-size:14px;color:var(--ink)}
.nav span{position:absolute;white-space:nowrap}
.cart{left:990px;top:0;width:80px;height:100px;background:var(--red);display:flex;align-items:center;justify-content:center}

/* hero */
.hero{top:100px;left:0;width:1200px;height:536px;
  background:
    radial-gradient(ellipse 380px 300px at 40% 45%,rgba(248,196,70,.9),transparent 70%),
    radial-gradient(ellipse 420px 260px at 10% 20%,rgba(40,150,200,.9),transparent 70%),
    radial-gradient(ellipse 500px 220px at 30% 100%,rgba(200,60,120,.85),transparent 70%),
    radial-gradient(ellipse 300px 200px at 0% 95%,rgba(110,60,150,.9),transparent 70%),
    radial-gradient(ellipse 400px 200px at 85% 0%,rgba(230,110,60,.9),transparent 70%),
    radial-gradient(ellipse 400px 200px at 100% 100%,rgba(210,60,110,.9),transparent 70%),
    linear-gradient(110deg,#2e6aa6 0%,#3f9fc6 22%,#eaa53a 42%,#ee7b33 58%,#e25a55 82%,#8a3a8f 100%)}
.hero h1{left:131px;top:152px;font-family:"Raleway",Arial,sans-serif;font-weight:700;font-size:46px;line-height:58px;color:var(--white)}
.hero .btn{left:131px;top:355px;width:118px;height:35px}
.hero-photo{left:614px;top:40px;width:586px;height:446px;
  background:
    radial-gradient(ellipse 200px 150px at 62% 50%,rgba(250,250,252,.95),rgba(230,236,242,.6) 60%,transparent 85%),
    radial-gradient(ellipse 120px 80px at 80% 45%,rgba(240,200,60,.55),transparent 80%),
    radial-gradient(ellipse 160px 120px at 20% 80%,rgba(40,70,110,.9),transparent 80%),
    linear-gradient(135deg,#132a48 0%,#2b4a72 45%,#4f6f93 70%,#263e5e 100%)}
.dots{display:flex;gap:8px}
.dots i{display:block;width:44px;height:3px;background:rgba(255,255,255,.85)}
.dots i:first-child{background:var(--red)}

/* services */
.services{top:636px;left:0;width:1200px;height:304px}
.services .title{top:40px}
.sub{top:90px;left:0;width:1200px;text-align:center;font-size:14px;color:var(--text)}
.svc{top:155px;width:200px;text-align:center;font-size:14px;color:var(--muted);line-height:18px}
.svc svg{display:block;margin:0 auto 8px}
.divider{top:142px;width:1px;height:110px;background:var(--line)}
.arrow{width:26px;height:26px;border:2px solid var(--ink);border-radius:50%;display:flex;align-items:center;justify-content:center}

/* portfolio */
.portfolio{top:940px;left:0;width:1200px;height:426px;background:linear-gradient(180deg,#f8f8f8,#e8e8e8)}
.portfolio .title{top:30px}
.card{top:100px}
.card .img{height:195px}
.card .label{height:65px;background:var(--black);color:var(--white);font-size:14px;display:flex;align-items:center;justify-content:center}
.img-brochure{background:
  radial-gradient(ellipse 90px 70px at 30% 55%,rgba(250,250,250,.95),transparent 80%),
  radial-gradient(ellipse 70px 80px at 70% 60%,rgba(245,245,245,.9),transparent 80%),
  radial-gradient(ellipse 60px 30px at 25% 15%,rgba(80,70,130,.8),transparent 80%),
  radial-gradient(ellipse 50px 50px at 90% 30%,rgba(120,160,100,.7),transparent 80%),
  linear-gradient(135deg,#cfc8dc,#a49cc0)}
.img-book{background:
  radial-gradient(ellipse 120px 70px at 50% 45%,rgba(245,245,248,.95),transparent 80%),
  radial-gradient(ellipse 60px 40px at 35% 35%,rgba(60,120,180,.7),transparent 80%),
  radial-gradient(ellipse 150px 50px at 50% 95%,rgba(90,55,30,.9),transparent 80%),
  linear-gradient(180deg,#6c5a4a,#a08466 50%,#5a3a22)}
.img-cards{background:
  radial-gradient(ellipse 80px 60px at 60% 50%,rgba(252,252,252,.95),transparent 80%),
  radial-gradient(ellipse 70px 40px at 25% 75%,rgba(248,248,248,.9),transparent 80%),
  radial-gradient(ellipse 60px 30px at 25% 15%,rgba(245,245,245,.85),transparent 80%),
  linear-gradient(135deg,#8a8fbc,#aab0d4 50%,#7f85b3)}
.portfolio .dots i{background:#bbb}
.portfolio .dots i:first-child{background:var(--red)}

/* cta */
.cta{top:1370px;left:0;width:1200px;height:150px;background:var(--red);color:var(--white);text-align:center}
.cta h2{margin-top:42px;font-family:"Raleway",Arial,sans-serif;font-weight:400;font-size:29px}
.cta p{margin-top:8px;font-size:14px}

/* submit job */
.job{top:1524px;left:0;width:1200px;height:518px;background:#4a4a4a}
.job-scene{left:0;top:0;width:1200px;height:518px;background:
  radial-gradient(ellipse 240px 200px at 14% 60%,rgba(40,160,160,.95),transparent 80%),
  radial-gradient(ellipse 300px 170px at 72% 62%,rgba(235,235,235,.9),transparent 80%),
  radial-gradient(ellipse 160px 150px at 40% 60%,rgba(210,210,210,.55),transparent 80%),
  radial-gradient(ellipse 60px 240px at 90% 35%,rgba(230,100,40,.95),transparent 85%),
  linear-gradient(180deg,#4b4b4b 0%,#3c3c3c 30%,#555 70%,#3a3a3a 100%)}
.job h2{top:30px;left:0;width:1200px;text-align:center;color:var(--white);font-family:"Raleway",Arial,sans-serif;font-weight:600;font-size:24px}
.job h2::after{content:"";display:block;width:46px;height:2px;background:var(--white);margin:10px auto 0}
.field{left:448px;width:302px;background:var(--white);font-size:10px;color:#555;padding:0 14px;display:flex;align-items:center;justify-content:space-between}
.job .btn{left:448px;top:432px;width:116px;height:35px}

/* books */
.books{top:2042px;left:0;width:1200px;height:538px;background:linear-gradient(180deg,#f6f6f6,#e6e6e6)}
.books .title{top:56px}
.cover{top:129px;width:197px;height:299px;box-shadow:0 6px 14px rgba(0,0,0,.25)}
.cover-one{background:
  radial-gradient(circle 34px at 50% 45%,rgba(200,30,30,.95),transparent 100%),
  radial-gradient(ellipse 90px 70px at 50% 72%,rgba(150,100,60,.9),transparent 85%),
  linear-gradient(180deg,#8a5a38,#4a2c1a 60%,#2a1a10)}
.cover-two{background:
  radial-gradient(ellipse 70px 130px at 50% 55%,rgba(20,25,60,.92),transparent 85%),
  linear-gradient(180deg,#f7a91c,#e4860f)}
.cover-three{background:
  radial-gradient(ellipse 90px 50px at 50% 30%,rgba(250,190,70,.85),transparent 85%),
  radial-gradient(ellipse 100px 90px at 50% 80%,rgba(160,60,150,.9),transparent 85%),
  linear-gradient(180deg,#2a8db2,#5a4f9a 60%,#3a2a5a)}
.books .btn{left:540px;top:468px;width:116px;height:32px}

/* about */
.about{top:2580px;left:0;width:1200px;height:389px}
.about h2{left:286px;top:68px;font-family:"Raleway",Arial,sans-serif;font-weight:500;font-size:25px;color:var(--red)}
.about p{left:131px;top:122px;width:455px;font-size:12.5px;line-height:17.6px;color:var(--ink)}
.about .btn{left:131px;top:284px;width:118px;height:31px}
.about-photo{left:614px;top:65px;width:455px;height:262px;background:
  radial-gradient(ellipse 180px 90px at 60% 55%,rgba(245,245,245,.95),transparent 80%),
  radial-gradient(ellipse 80px 120px at 12% 30%,rgba(50,45,40,.9),transparent 85%),
  radial-gradient(ellipse 90px 60px at 40% 85%,rgba(200,150,120,.6),transparent 85%),
  linear-gradient(135deg,#5a5550,#b9b5b0 50%,#8a8682)}

/* footer */
.footer{top:2969px;left:0;width:1200px;height:277px;background:var(--black);color:var(--white)}
.fcol{top:60px}
.fcol h3{font-family:"Raleway",Arial,sans-serif;font-weight:600;font-size:17px;margin-bottom:22px}
.fcol ul{list-style:none;font-size:11px;line-height:33px}
.fsep{top:42px;width:1px;height:160px;background:#444}
.contact li{display:flex;align-items:center;gap:12px;line-height:16px;margin-bottom:14px}
.news-input{left:846px;top:100px;width:221px;height:33px;background:#3a3a3a;font-size:10px;padding:0 14px;display:flex;align-items:center}
.news-send{left:1014px;top:144px;width:53px;height:35px;background:var(--red);display:flex;align-items:center;justify-content:center}
.bottom{top:3246px;left:0;width:1200px;height:33px;background:#000;color:#ddd;font-size:10px}
.bottom .legal{left:131px;top:10px;font-style:italic;display:flex;gap:26px}
.bottom .copy{left:480px;top:10px;font-style:italic}
.social{left:990px;top:11px;display:flex;gap:6px}
.social i{display:block;width:11px;height:11px;background:#ddd}
</style>
</head>
<body>

<header class="header abs">
  <div class="brand abs"><span class="brand-mark"></span><span class="brand-name">VINDABROT</span></div>
  <div class="topline abs">
    <svg width="14" height="14" viewBox="0 0 24 24"><path d="M6.6 10.8a15 15 0 006.6 6.6l2.2-2.2c.3-.3.7-.4 1-.2 1.1.4 2.3.6 3.6.6.6 0 1 .4 1 1V20c0 .6-.4 1-1 1A17 17 0 013 4c0-.6.4-1 1-1h3.5c.6 0 1 .4 1 1 0 1.3.2 2.5.6 3.6.1.3 0 .7-.2 1z" fill="#c93a2b"/></svg>
    <span class="call">Call Us</span><span>555 0142</span>
  </div>
  <nav class="nav abs">
    <span style="left:0">Home</span>
    <span style="left:92px">Services <svg width="10" height="8" viewBox="0 0 10 8"><path d="M1 2l4 4 4-4" stroke="#333" fill="none" stroke-width="1.4"/></svg></span>
    <span style="left:218px">Portfolio <svg width="10" height="8" viewBox="0 0 10 8"><path d="M1 2l4 4 4-4" stroke="#333" fill="none" stroke-width="1.4"/></svg></span>
    <span style="left:345px">Submit Job</span>
    <span style="left:472px">Online Books <svg width="10" height="8" viewBox="0 0 10 8"><path d="M1 2l4 4 4-4" stroke="#333" fill="none" stroke-width="1.4"/></svg></span>
    <span style="left:614px">About Us</span>
  </nav>
  <div class="cart abs">
    <svg width="24" height="26" viewBox="0 0 24 26"><path d="M4 8h16l-1 16H5z" fill="none" stroke="#fff" stroke-width="1.8"/><path d="M8 11V6a4 4 0 018 0v5" fill="none" stroke="#fff" stroke-width="1.8"/></svg>
  </div>
</header>

<section class="hero abs">
  <h1 class="abs">Let Us Help<br>You With All Of Your<br>Printing Needs</h1>
  <div class="btn abs">Order Online</div>
  <div class="hero-photo abs" role="img" aria-label="Open printed magazine lying on a printing press"></div>
  <div class="dots abs" style="left:524px;top:510px"><i></i><i></i><i></i></div>
</section>

<section class="services abs">
  <h2 class="title abs">Services</h2>
  <p class="sub abs">Online and in store, you can find printing services to help you get the job done</p>
  <div class="arrow abs" style="left:131px;top:182px"><svg width="10" height="10" viewBox="0 0 10 10"><path d="M6.5 1.5L3 5l3.5 3.5" stroke="#1d1d1d" stroke-width="1.8" fill="none"/></svg></div>
  <div class="svc abs" style="left:200px">
    <svg width="54" height="52" viewBox="0 0 54 52"><rect x="4" y="6" width="44" height="12" fill="#d9453a"/><rect x="8" y="20" width="42" height="12" fill="#3a9d6a"/><rect x="4" y="34" width="46" height="12" fill="#f2a31b"/></svg>
    Book<br>Printing
  </div>
  <div class="divider abs" style="left:440px"></div>
  <div class="svc abs" style="left:508px">
    <svg width="64" height="56" viewBox="0 0 64 56"><path d="M4 8l18-6v46L4 54z" fill="#3e8a2e"/><path d="M22 2l20 6v46l-20-6z" fill="#6cbf3a"/><path d="M42 8l18-6v46l-18 6z" fill="#3e8a2e"/><rect x="26" y="16" width="12" height="10" fill="#f2c21b"/></svg>
    Brochure<br>Printing
  </div>
  <div class="divider abs" style="left:755px"></div>
  <div class="svc abs" style="left:806px">
    <svg width="44" height="52" viewBox="0 0 44 52"><rect x="6" y="10" width="32" height="38" fill="#e7e7e7"/><rect x="14" y="18" width="16" height="16" fill="#3a6fb0"/><rect x="12" y="38" width="20" height="4" fill="#3a6fb0"/><rect x="19" y="2" width="6" height="10" fill="#555"/></svg>
    Business card<br>Printing
  </div>
  <div class="arrow abs" style="left:1041px;top:182px"><svg width="10" height="10" viewBox="0 0 10 10"><path d="M3.5 1.5L7 5 3.5 8.5" stroke="#1d1d1d" stroke-width="1.8" fill="none"/></svg></div>
</section>

<section class="portfolio abs">
  <h2 class="title abs">PortFolio</h2>
  <div class="card abs" style="left:131px;width:309px"><div class="img img-brochure" role="img" aria-label="Brochure mockup on a desk"></div><div class="label">Brochure</div></div>
  <div class="card abs" style="left:448px;width:304px"><div class="img img-book" role="img" aria-label="Open printed book on a wooden table"></div><div class="label">Book Printing</div></div>
  <div class="card abs" style="left:761px;width:306px"><div class="img img-cards" role="img" aria-label="Stacks of business cards on a lilac surface"></div><div class="label">Business Card</div></div>
  <div class="dots abs" style="left:524px;top:390px"><i></i><i></i><i></i></div>
</section>

<section class="cta abs">
  <h2>Unleash Your Ideas.&nbsp; We'll help You</h2>
  <p>Through simplicity and flexibility of our services can be reached quickly and easily to your pressure.</p>
</section>

<section class="job abs">
  <div class="job-scene abs" role="img" aria-label="Brochure mockups and a feather pen on a grey surface"></div>
  <h2 class="abs">Submit Us Job</h2>
  <div class="field abs" style="top:89px;height:35px">Name</div>
  <div class="field abs" style="top:144px;height:33px">Email</div>
  <div class="field abs" style="top:194px;height:35px">Phone Number</div>
  <div class="field abs" style="top:251px;height:37px">Upload Files
    <svg width="14" height="12" viewBox="0 0 14 12"><rect x="1" y="3" width="12" height="8" fill="none" stroke="#555"/><circle cx="7" cy="7" r="2" fill="none" stroke="#555"/><rect x="4" y="1" width="6" height="2" fill="#555"/></svg></div>
  <div class="field abs" style="top:306px;height:100px;align-items:flex-start;padding-top:14px">Message</div>
  <div class="btn abs">Send</div>
</section>

<section class="books abs">
  <h2 class="title abs">Online Books</h2>
  <div class="arrow abs" style="left:131px;top:269px"><svg width="10" height="10" viewBox="0 0 10 10"><path d="M6.5 1.5L3 5l3.5 3.5" stroke="#1d1d1d" stroke-width="1.8" fill="none"/></svg></div>
  <div class="cover cover-one abs" style="left:221px" role="img" aria-label="Book cover with a red apple on a stack of old books"></div>
  <div class="cover cover-two abs" style="left:503px" role="img" aria-label="Book cover with a dark silhouette on orange"></div>
  <div class="cover cover-three abs" style="left:785px" role="img" aria-label="Illustrated adventure book cover in teal and purple"></div>
  <div class="arrow abs" style="left:1041px;top:269px"><svg width="10" height="10" viewBox="0 0 10 10"><path d="M3.5 1.5L7 5 3.5 8.5" stroke="#1d1d1d" stroke-width="1.8" fill="none"/></svg></div>
  <div class="btn abs">Order Online</div>
</section>

<section class="about abs">
  <h2 class="abs">About Us</h2>
  <p class="abs">Vindabrot is a company located on the university campus, which has specialized in servicing school staff, as well as providing general public printing.<br>Vindabrot prints out first-class textbooks for seminars, thesis for doctors-,masters- and bachelors-degrees, plus working on whole lot of smaller pieces for students, teachers and organizations. These include brochures, reports, questionnaires, business cards, books, OCR scanning and more.</p>
  <div class="btn abs">Read More</div>
  <div class="about-photo abs" role="img" aria-label="Printed magazines spread on a table"></div>
</section>

<footer class="footer abs">
  <div class="fcol abs" style="left:214px"><h3>Menu</h3><ul><li>Home</li><li>Service</li><li>Portfolio</li><li>Online Books</li></ul></div>
  <div class="fsep abs" style="left:365px"></div>
  <div class="fcol abs" style="left:438px"><h3>Services</h3><ul><li>Book Printing</li><li>Business Cards</li><li>Brochure Printing</li><li>Flyers &amp; Text books</li></ul></div>
  <div class="fsep abs" style="left:597px"></div>
  <div class="fcol abs contact" style="left:645px"><h3 style="margin-left:28px">Contact</h3>
    <ul>
      <li><svg width="12" height="16" viewBox="0 0 12 16"><path d="M6 0a6 6 0 016 6c0 4-6 10-6 10S0 10 0 6a6 6 0 016-6z" fill="#fff"/><circle cx="6" cy="6" r="2.2" fill="#0e0e0e"/></svg><span>Lindargata 9,<br>101 Reykjavík</span></li>
      <li><svg width="12" height="12" viewBox="0 0 24 24"><path d="M6.6 10.8a15 15 0 006.6 6.6l2.2-2.2c.3-.3.7-.4 1-.2 1.1.4 2.3.6 3.6.6.6 0 1 .4 1 1V20c0 .6-.4 1-1 1A17 17 0 013 4c0-.6.4-1 1-1h3.5c.6 0 1 .4 1 1 0 1.3.2 2.5.6 3.6.1.3 0 .7-.2 1z" fill="#fff"/></svg><span>555 0142</span></li>
      <li><svg width="14" height="10" viewBox="0 0 14 10"><rect width="14" height="10" fill="#fff"/><path d="M0 0l7 5 7-5" stroke="#0e0e0e" fill="none"/></svg><span>info@vindabrot.is</span></li>
    </ul>
  </div>
  <div class="fsep abs" style="left:831px"></div>
  <div class="fcol abs" style="left:896px"><h3>News Letter</h3></div>
  <div class="news-input abs">Query</div>
  <div class="news-send abs"><svg width="18" height="16" viewBox="0 0 18 16"><path d="M1 8L17 1l-4 14-4-5z" fill="none" stroke="#fff" stroke-width="1.4"/><path d="M9 10L17 1" stroke="#fff" stroke-width="1.4"/></svg></div>
</footer>

<div class="bottom abs">
  <div class="legal abs"><span>Terms Conditions</span><span>Privacy Policy</span></div>
  <div class="copy abs">Copyright by Vindabrot. All Right Reserved © 2018</div>
  <div class="social abs"><i></i><i></i><i></i><i></i></div>
</div>

</body>
</html>
```